Buch-/eBook-Cover für Traumatherapeutin
Zielgruppe
Ich bin Traumatherapeutin und schreibe ein Buch zum Thema Trauma bearbeiten.
Meine Zielgruppe sucht Heilung, Genesung, Selbstliebe etc.
Aufgabenstellung
Buchcover
Bitte erstell mir ein modernes positives inspirierendes Buchcover mit dem
Titel: 'Morgens LEISE aufbrechen“
Untertitel: „Geh den Pfad, der dich leise ruft“
Dr. Merle Kuhnast
Ich hätte gerne ein modernes Buch, das entweder einen Bezug zum Thema Trauma hat oder aber einfach stylische Schriftzüge. Bin aber auch offen für andere Vorschläge.
Dunkelblau, weiß und türkis oder auch rosa mag ich ganz gerne. Wobei Dunkelblau, weiß und türkis meine Favoriten sind und mit rosa höchstens kleinere Akzente gesetzt werden sollten.
Das Buchcover soll modern sein und direkt ansprechen. Gerne eine originelle Lösung, oder etwas Besonderes, etwas das Tiefe ausdrückt, oder man mehrmals hinsehen muss um etwas zu erkennen oder etwas das mehr Interpretationsspielraum lässt.
Gerne auch viel weiß, zumindest heller und nicht zu dunkel. Stylish, aber nicht überfrachtet.
Schreib mich gerne an, wenn du Fragen hast.
Ich habe mal zwei Beispiel von Typolösungen angehängt, die ich ganz cool fände.
Ich freue mich auf deine Ideen :-)
Ganz liebe Grüße
Merle

```html
<!DOCTYPE html>
<html lang="de">
<head>
<meta charset="utf-8">
<title>Morgens LEISE aufbrechen – Dr. Merle Kuhnast</title>
<link rel="stylesheet" href="https://fonts.googleapis.com/css2?family=Allura&family=Bebas+Neue&family=Open+Sans:ital,wght@0,400;1,400&display=swap">
<style>
  :root {
    --rose: #d3a2c0;
    --mist: #b9c3cd;
    --mint: #a9d9d2;
    --mint-deep: #a4d6cf;
    --violet: #5b3a93;
    --white: #ffffff;
  }
  html, body {
    margin: 0;
    padding: 0;
    width: 858px;
    height: 1200px;
    overflow: hidden;
  }
  .cover {
    position: relative;
    width: 858px;
    height: 1200px;
    overflow: hidden;
    background: linear-gradient(160deg, var(--rose) 0%, var(--mist) 33%, var(--mint) 62%, var(--mint-deep) 100%);
  }
  .author {
    position: absolute;
    top: 50px;
    left: 0;
    width: 100%;
    text-align: center;
    font-family: "Open Sans", sans-serif;
    font-size: 23px;
    color: var(--white);
    letter-spacing: 0.2px;
  }
  .title-script {
    position: absolute;
    margin: 0;
    font-family: "Allura", cursive;
    font-weight: 400;
    color: var(--violet);
    line-height: 1;
  }
  .title-top {
    left: 98px;
    top: 398px;
    font-size: 100px;
  }
  .title-bottom {
    left: 318px;
    top: 652px;
    font-size: 100px;
  }
  .title-main {
    position: absolute;
    left: 128px;
    top: 478px;
    margin: 0;
    font-family: "Bebas Neue", sans-serif;
    font-weight: 400;
    font-size: 222px;
    line-height: 1;
    color: var(--white);
    letter-spacing: 1px;
  }
  .subtitle {
    position: absolute;
    right: 112px;
    top: 764px;
    margin: 0;
    text-align: right;
    font-family: "Open Sans", sans-serif;
    font-style: italic;
    font-size: 25px;
    line-height: 36px;
    color: var(--violet);
  }
  .badge {
    position: absolute;
    left: 540px;
    top: 962px;
  }
</style>
</head>
<body>
  <main class="cover">
    <p class="author">Dr. Merle Kuhnast</p>
    <h1>
      <span class="title-script title-top">Morgens</span>
      <span class="title-main">LEISE</span>
      <span class="title-script title-bottom">aufbrechen</span>
    </h1>
    <p class="subtitle">Geh den Pfad, der dich leise ruft<br>auf deinem eigenen Weg</p>
    <svg class="badge" width="318" height="128" viewBox="0 0 318 128" aria-hidden="true">
      <polygon points="52,0 318,0 318,128 0,128" fill="var(--violet)"/>
    </svg>
  </main>
</body>
</html>
```